Stationary for Vornik Consulting

Hi

I am after stationary designs for my company - Vornik Consulting. I have a logo - recently designed by PixelHarbor. Vornik ( sales spelt backwards ) is a sales consultancy - including sales training, sales coaching and business management.

I have attached some of the artwork I already have, as well as a few ideas
1. Use supplied logo's
2. back of business card to use the logo with the dark background and white text
3. details to be included on card are
Logo
Delmo Kastrani
p: +61409371826
e: delmo@vornikconsulting.com.au
w: www.vornikconsulting.com.au
PO Box 417, Balwyn North, Victoria, 3104

4. I am after designs for business cards, A4 letterhead and A5 letterhead

Thanks in Advance

Delmo

```html
<!DOCTYPE html>
<html lang="en">
<head>
<meta charset="utf-8">
<title>Vornik Consulting Stationery</title>
<link rel="stylesheet" href="https://fonts.googleapis.com/css2?family=Montserrat:wght@600;700&family=Open+Sans:wght@400;600&display=swap">
<style>
:root{
  --navy:#2e4350;
  --orange:#e4441f;
  --paper:#ffffff;
  --bg:#ececec;
  --ink:#4a4f55;
  --muted:#8a8f94;
}
*{box-sizing:border-box;margin:0;padding:0}
html,body{width:1200px;height:795px;overflow:hidden;background:var(--bg)}
body{position:relative;font-family:"Open Sans",Arial,sans-serif;color:var(--ink)}
.sheet{position:absolute;background:var(--paper);overflow:hidden;box-shadow:0 2px 8px rgba(0,0,0,.15)}
.brand{font-family:"Montserrat",Arial,sans-serif;font-weight:700;color:var(--navy);display:flex;align-items:center;gap:6px;white-space:nowrap}
.brand-mark{background:var(--orange);flex:none}
.brand--light{color:#fff}

/* Plain footer band */
.footer-band{position:absolute;left:0;right:0;bottom:0;background:var(--navy);border-top:solid var(--orange)}

/* Letterheads */
.letterhead-a4{left:40px;top:40px;width:380px;height:537px;padding:26px 28px}
.letterhead-a5{left:450px;top:40px;width:280px;height:396px;padding:20px 20px}
.lh-top{display:flex;justify-content:space-between;align-items:flex-start;gap:10px}
.lh-contact{text-align:right;font-size:5.5px;line-height:1.6;color:var(--muted);border-bottom:1px solid var(--orange);padding-bottom:3px;white-space:nowrap}
.letterhead-a5 .lh-contact{font-size:4.4px}
.letter{margin-top:18px;font-size:6.4px;line-height:1.55}
.letterhead-a5 .letter{margin-top:14px;font-size:5.2px}
.letter p{margin-bottom:7px}
.recipient{margin-bottom:9px}
.recipient strong{font-weight:600;color:var(--navy)}
.signature{width:60px;height:16px;background:linear-gradient(90deg,#d9dadb,#eeeeee);margin:4px 0}
.letterhead-a5 .signature{width:46px;height:12px}
.letterhead-a4 .brand{font-size:15px}
.letterhead-a4 .brand-mark{width:8px;height:8px}
.letterhead-a5 .brand{font-size:11px}
.letterhead-a5 .brand-mark{width:6px;height:6px}
.letterhead-a4 .footer-band{height:26px;border-top-width:4px}
.letterhead-a5 .footer-band{height:20px;border-top-width:3px}

/* Business cards */
.card{width:230px;height:146px}
.card-back{left:450px;top:468px}
.card-front{left:450px;top:630px}
.card-back .brand{position:absolute;left:24px;top:44px;font-size:17px}
.card-back .brand-mark{width:9px;height:9px}
.card-back .footer-band{height:34px;border-top-width:4px}
.card-front .brand{position:absolute;left:14px;top:34px;font-size:11px}
.card-front .brand-mark{width:6px;height:6px}
.card-front .footer-band{height:12px;border-top-width:3px}
.holder{position:absolute;right:14px;top:12px;text-align:right}
.holder-name{font-family:"Montserrat",Arial,sans-serif;font-weight:600;font-size:10px;color:var(--orange)}
.holder-role{font-size:6px;color:var(--muted)}
.card-details{position:absolute;left:14px;top:56px;list-style:none;font-size:5.6px;line-height:1.75;color:var(--ink)}
.card-details li{display:flex;align-items:center;gap:4px}
.card-details svg{width:6px;height:6px;flex:none}

/* Envelopes */
.envelope{width:400px;height:200px}
.envelope-back{left:760px;top:40px}
.envelope-front{left:760px;top:270px}
.flap{position:absolute;left:0;right:0;top:0;height:72px;background:var(--navy);border-radius:0 0 24px 24px}
.envelope-back .brand{position:absolute;left:50%;top:36px;transform:translateX(-50%);font-size:14px}
.envelope-back .brand-mark{width:7px;height:7px}
.side-band{position:absolute;top:0;bottom:0;right:0;width:70px;background:var(--navy);border-left:5px solid var(--orange)}
.envelope-front .brand{position:absolute;left:22px;top:118px;font-size:14px}
.envelope-front .brand-mark{width:7px;height:7px}
.return-address{position:absolute;left:22px;top:140px;font-size:5.6px;line-height:1.6;color:var(--ink)}
</style>
</head>
<body>

<section class="sheet letterhead-a4" aria-label="A4 letterhead">
  <div class="lh-top">
    <div class="brand"><span class="brand-mark"></span>Vornik Consulting</div>
    <div class="lh-contact">
      p: +61409371826 | e: delmo@vornikconsulting.com.au<br>
      w: www.vornikconsulting.com.au<br>
      PO Box 417, Balwyn North, Victoria, 3104
    </div>
  </div>
  <div class="letter">
    <div class="recipient">To,<br><strong>Mr. Tomas Reale</strong><br>Operations Director<br>Reale Logistics</div>
    <p>Thank you for meeting with our team last week. We have outlined a sales coaching plan that suits your staff and your current growth targets.</p>
    <p>The program runs over twelve weeks and covers prospecting, negotiation and account planning, with short review sessions after each stage to track progress.</p>
    <p>We would be glad to discuss the details further at a time that suits you. Please contact me directly with any questions.</p>
    <p>Thanks and Regards,</p>
    <div class="signature" role="img" aria-label="Handwritten signature"></div>
  </div>
  <div class="footer-band"></div>
</section>

<section class="sheet letterhead-a5" aria-label="A5 letterhead">
  <div class="lh-top">
    <div class="brand"><span class="brand-mark"></span>Vornik Consulting</div>
    <div class="lh-contact">
      p: +61409371826 | e: delmo@vornikconsulting.com.au<br>
      w: www.vornikconsulting.com.au<br>
      PO Box 417, Balwyn North, Victoria, 3104
    </div>
  </div>
  <div class="letter">
    <div class="recipient">To,<br><strong>Mr. Tomas Reale</strong><br>Operations Director<br>Reale Logistics</div>
    <p>Thank you for meeting with our team last week. We have outlined a sales coaching plan that suits your staff and your current growth targets.</p>
    <p>The program runs over twelve weeks and covers prospecting, negotiation and account planning, with short review sessions after each stage to track progress.</p>
    <p>We would be glad to discuss the details further at a time that suits you. Please contact me directly with any questions.</p>
    <p>Thanks and Regards,</p>
    <div class="signature" role="img" aria-label="Handwritten signature"></div>
  </div>
  <div class="footer-band"></div>
</section>

<section class="sheet card card-back" aria-label="Business card back">
  <div class="brand"><span class="brand-mark"></span>Vornik Consulting</div>
  <div class="footer-band"></div>
</section>

<section class="sheet card card-front" aria-label="Business card front">
  <div class="holder">
    <div class="holder-name">Delmo Kastrani</div>
    <div class="holder-role">Director</div>
  </div>
  <div class="brand"><span class="brand-mark"></span>Vornik Consulting</div>
  <ul class="card-details">
    <li><svg viewBox="0 0 10 10"><rect width="10" height="10" rx="2" fill="var(--navy)"/></svg>p: +61409371826</li>
    <li><svg viewBox="0 0 10 10"><rect width="10" height="10" rx="2" fill="var(--navy)"/></svg>e: delmo@vornikconsulting.com.au</li>
    <li><svg viewBox="0 0 10 10"><rect width="10" height="10" rx="2" fill="var(--navy)"/></svg>w: www.vornikconsulting.com.au</li>
    <li><svg viewBox="0 0 10 10"><path d="M5 0a3.6 3.6 0 0 0-3.6 3.6C1.4 6.5 5 10 5 10s3.6-3.5 3.6-6.4A3.6 3.6 0 0 0 5 0z" fill="var(--navy)"/></svg>PO Box 417, Balwyn North, Victoria, 3104</li>
  </ul>
  <div class="footer-band"></div>
</section>

<section class="sheet envelope envelope-back" aria-label="Envelope back">
  <div class="flap"></div>
  <div class="brand brand--light"><span class="brand-mark"></span>Vornik Consulting</div>
</section>

<section class="sheet envelope envelope-front" aria-label="Envelope front">
  <div class="side-band"></div>
  <div class="brand"><span class="brand-mark"></span>Vornik Consulting</div>
  <div class="return-address">
    e: delmo@vornikconsulting.com.au<br>
    w: www.vornikconsulting.com.au<br>
    PO Box 417, Balwyn North, Victoria, 3104
  </div>
</section>

</body>
</html>
```